Trading company needs a non alcoholic beer Can design

We KLM are trading company , food Distributors in Africa -RD Congo/Kinshasa .We want to do a Private label non alcoholic beer 500ml can and need a design for this Project .
the Brand Name is : NUVA BREW
We want it to be similar NOT a copy of Velmora 0.0% can ( picture
attached ) as we want to respect the intellectual properties .so we prefer to use the same colors but more elegant ,modern style .
thanks.
THE DESIGN MUST STATE ITS A NON ALCOHOLIC BEER
PLZ SEARCH FOR VELMORA 0.0% MALT DRINK YOU WILL FIND 2 DESIGNS OLD AND NEW WE NEED SOMTHING SIMILAR TO THESE DESIGNS ,KINDLY USE SAME COLORS AND THE 0.0% SHOULD BE IN THE MIDDLE OF THE CAN .
Target Market(s)
THE PRODUCT WILL BE SOLD IN THE SUPERMASRKTS / MODERN TRADE

```html
<!DOCTYPE html>
<html lang="en">
<head>
<meta charset="utf-8">
<title>NUVA BREW 0.0% Non Alcoholic Beer – Can Label</title>
<link href="https://fonts.googleapis.com/css2?family=Playfair+Display:wght@600&family=Great+Vibes&family=Montserrat:ital,wght@0,600;0,700;1,800;1,900&display=swap" rel="stylesheet">
<style>
  :root {
    --bg: #e6e7e8;
    --red-deep: #a8260f;
    --red-mid: #c7401f;
    --red-light: #df5a33;
    --royal: #1f3f9c;
    --royal-dark: #162d78;
    --gold: #d8ae4a;
    --cream: #f3f3f1;
    --blue-num: #2f67b5;
    --blue-num-light: #8fb6e6;
    --white: #ffffff;
  }
  * { margin: 0; padding: 0; box-sizing: border-box; }
  html, body { width: 960px; height: 1200px; overflow: hidden; }
  body { background: var(--bg); position: relative; font-family: "Montserrat", sans-serif; }

  .can-label {
    position: absolute; left: 240px; top: 30px; width: 480px; height: 1140px;
    border-radius: 18px; overflow: hidden;
    background: linear-gradient(100deg, var(--red-deep) 0%, var(--red-mid) 30%, var(--red-light) 48%, var(--red-mid) 66%, var(--red-deep) 100%);
  }
  .stripe-texture {
    position: absolute; inset: 0;
    background: linear-gradient(160deg, rgba(255,255,255,0.06), rgba(0,0,0,0.08));
  }

  .seal { position: absolute; left: 198px; top: 226px; width: 84px; height: 84px; }

  .brand-plaque { position: absolute; left: 6px; top: 300px; width: 468px; height: 260px; }
  .brand-name {
    position: absolute; left: 0; right: 0; top: 382px; text-align: center;
    font-family: "Playfair Display", serif; font-weight: 600; font-size: 64px;
    color: var(--white); letter-spacing: -1px; line-height: 1;
  }
  .brand-sub {
    position: absolute; left: 0; right: 0; top: 458px; text-align: center;
    font-family: "Great Vibes", cursive; font-size: 34px; color: var(--white); line-height: 1;
  }

  .alc-band { position: absolute; left: 0; top: 575px; width: 480px; height: 265px; }
  .alc-figure {
    position: absolute; left: 80px; top: 640px;
    font-weight: 900; font-style: italic; font-size: 150px; line-height: 1; letter-spacing: -6px;
    background: linear-gradient(180deg, var(--blue-num-light) 0%, var(--blue-num) 48%, var(--royal-dark) 100%);
    -webkit-background-clip: text; background-clip: text; color: transparent;
  }
  .alc-percent {
    position: absolute; left: 300px; top: 612px;
    font-weight: 900; font-style: italic; font-size: 92px; line-height: 1; color: var(--blue-num);
  }
  .alc-label {
    position: absolute; left: 298px; top: 712px;
    font-weight: 800; font-style: italic; font-size: 30px; line-height: 1; color: var(--blue-num);
  }

  .product-info { position: absolute; left: 0; right: 0; top: 895px; text-align: center; color: var(--white); }
  .product-tier { font-weight: 700; font-size: 24px; letter-spacing: 2px; line-height: 1; }
  .product-name { font-weight: 600; font-size: 46px; letter-spacing: 1px; line-height: 1; margin-top: 10px; }
  .product-type { font-weight: 600; font-size: 15px; letter-spacing: 0.5px; margin-top: 8px; }
  .product-rule { width: 110px; height: 2px; background: var(--white); margin: 10px auto 0; }
  .product-volume { font-weight: 700; font-style: italic; font-size: 24px; margin-top: 40px; }
</style>
</head>
<body>
  <main class="can-label">
    <div class="stripe-texture" role="img" aria-label="Red diagonal line pattern background"></div>

    <svg class="seal" viewBox="0 0 84 84" aria-hidden="true">
      <circle cx="42" cy="42" r="41" fill="var(--royal)"/>
      <circle cx="42" cy="42" r="28" fill="none" stroke="var(--gold)" stroke-width="3"/>
    </svg>

    <svg class="brand-plaque" viewBox="0 0 468 260" aria-hidden="true">
      <path d="M60 40 H180 Q234 10 288 40 H408 Q430 40 440 70 Q468 130 440 190 Q430 220 408 220 H288 Q234 250 180 220 H60 Q38 220 28 190 Q0 130 28 70 Q38 40 60 40 Z"
            fill="var(--cream)"/>
      <path d="M66 52 H182 Q234 24 286 52 H402 Q420 52 428 76 Q452 130 428 184 Q420 208 402 208 H286 Q234 236 182 208 H66 Q48 208 40 184 Q16 130 40 76 Q48 52 66 52 Z"
            fill="var(--royal)" stroke="var(--gold)" stroke-width="3"/>
    </svg>
    <div class="brand-name">NUVA BREW</div>
    <div class="brand-sub">Premium</div>

    <svg class="alc-band" viewBox="0 0 480 265" aria-hidden="true">
      <path d="M0 45 L40 38 L30 30 L110 28 L100 20 L220 22 L250 10 L300 16 L360 0 L400 6 L480 2
               L480 205 L440 212 L400 208 L330 225 L280 222 L220 240 L170 236 L120 252 L60 258 L20 265 L0 262 Z"
            fill="var(--cream)"/>
    </svg>
    <div class="alc-figure">0.0</div>
    <div class="alc-percent">%</div>
    <div class="alc-label">ALC.</div>

    <section class="product-info">
      <div class="product-tier">PREMIUM</div>
      <div class="product-name">ORIGINAL</div>
      <div class="product-type">NON ALCOHOLIC BEER</div>
      <div class="product-rule"></div>
      <div class="product-volume">500ml</div>
    </section>
  </main>
</body>
</html>
```